EXPEDITE! Business Card For a Private Equity Firm
Fresh and Sleek
EXPEDITE!  Business Card For a Private Equity Firm - Financial Services
Creative Brief
Bright & Fun-filled
Ned Rusholt
Managing Partner
712 Larkmoor Street New York, NY 10032
ned@vorumbra-example.com
www.vorumbra-example.com
Looking for a fresh look on our new business cards. We have had previous designs on Plenavox for similar companies, but, now is time to refresh the look! Please submit as many design as possible. We will give you fast, efficient feedback!
Vorumbra Vorumbra
All. We also need email signatures and letterhead. Please provide.

```html
<!DOCTYPE html>
<html lang="en">
<head>
<meta charset="utf-8">
<title>Vorumbra Business Card</title>
<link href="https://fonts.googleapis.com/css2?family=Lato:ital,wght@0,400;0,700;1,400&display=swap" rel="stylesheet">
<style>
  :root {
    --bg: #e9e7e3;
    --card: #ffffff;
    --card-edge: #dcdfe3;
    --brand: #2f86c6;
    --brand-soft: #9fc9e8;
    --silver: #b9bec6;
    --ink: #5b6470;
    --ink-light: #8a929c;
  }
  * { margin: 0; padding: 0; box-sizing: border-box; }
  html, body { width: 1200px; height: 1023px; overflow: hidden; }
  body {
    background: var(--bg);
    font-family: "Lato", sans-serif;
    color: var(--ink);
    display: flex;
    flex-direction: column;
    align-items: center;
    justify-content: center;
    gap: 56px;
  }
  .card {
    position: relative;
    width: 760px;
    height: 434px;
    background: var(--card);
    border: 1px solid var(--card-edge);
    box-shadow: 0 6px 18px rgba(0,0,0,0.12);
    overflow: hidden;
  }
  .decor {
    position: absolute;
    border-radius: 50%;
  }
  .card-front .decor {
    width: 620px; height: 380px;
    left: 70px; top: 27px;
    background: radial-gradient(ellipse at center, rgba(159,201,232,0.35) 0%, rgba(185,190,198,0.18) 45%, rgba(255,255,255,0) 72%);
  }
  .card-back .decor {
    width: 420px; height: 360px;
    right: -60px; bottom: -70px;
    background: radial-gradient(ellipse at center, rgba(47,134,198,0.45) 0%, rgba(159,201,232,0.35) 35%, rgba(185,190,198,0.25) 55%, rgba(255,255,255,0) 72%);
  }
  .brand {
    display: flex;
    align-items: center;
    gap: 10px;
    color: var(--brand);
    font-weight: 400;
    letter-spacing: 0.08em;
    text-transform: uppercase;
  }
  .brand-dot {
    border-radius: 50%;
    background: var(--brand);
  }
  .card-front .brand {
    position: absolute;
    left: 50%; top: 50%;
    transform: translate(-50%, -50%);
    font-size: 30px;
  }
  .card-front .brand-dot { width: 22px; height: 22px; }
  .card-back .brand {
    position: absolute;
    left: 50px; top: 40px;
    font-size: 38px;
  }
  .card-back .brand-dot { width: 26px; height: 26px; }
  .contact {
    position: absolute;
    left: 62px; top: 122px;
  }
  .person-name {
    font-style: italic;
    font-size: 19px;
    color: var(--brand);
  }
  .person-title {
    font-style: italic;
    font-size: 14px;
    color: var(--ink-light);
    margin-bottom: 12px;
  }
  .address {
    font-style: italic;
    font-size: 14px;
    line-height: 1.35;
    margin-bottom: 12px;
  }
  .lines { list-style: none; }
  .lines li {
    display: flex;
    align-items: center;
    gap: 10px;
    font-size: 14px;
    line-height: 1.65;
  }
  .lines svg { width: 14px; height: 14px; flex: none; }
</style>
</head>
<body>
  <section class="card card-front">
    <div class="decor" role="img" aria-label="Soft blue and silver decorative swirl area"></div>
    <div class="brand"><span class="brand-dot"></span>Vorumbra</div>
  </section>

  <section class="card card-back">
    <div class="decor" role="img" aria-label="Large blue and silver decorative swirl area"></div>
    <div class="brand"><span class="brand-dot"></span>Vorumbra</div>
    <div class="contact">
      <p class="person-name">Ned Rusholt</p>
      <p class="person-title">Managing Partner</p>
      <p class="address">712 Larkmoor Street<br>New York, NY 10032</p>
      <ul class="lines">
        <li><svg viewBox="0 0 14 14"><circle cx="7" cy="7" r="7" fill="#2f86c6"/><path d="M4.5 3.5l1.5 0 .6 1.8-1 .7a5 5 0 002.4 2.4l.7-1 1.8.6v1.5c0 .5-.4.8-.9.8A6.2 6.2 0 013.7 4.4c0-.5.3-.9.8-.9z" fill="#fff"/></svg>(212) 555-0143</li>
        <li><svg viewBox="0 0 14 14"><circle cx="7" cy="7" r="7" fill="#8a929c"/><rect x="4" y="5" width="6" height="4.5" fill="#fff"/><rect x="5" y="3.2" width="4" height="2" fill="#fff"/></svg>(212) 555-0178</li>
        <li><svg viewBox="0 0 14 14"><circle cx="7" cy="7" r="7" fill="#2f86c6"/><rect x="3.5" y="4.5" width="7" height="5" fill="none" stroke="#fff"/><path d="M3.5 4.5l3.5 3 3.5-3" fill="none" stroke="#fff"/></svg>ned@vorumbra-example.com</li>
        <li><svg viewBox="0 0 14 14"><circle cx="7" cy="7" r="7" fill="#8a929c"/><circle cx="7" cy="7" r="3.5" fill="none" stroke="#fff"/><path d="M3.5 7h7M7 3.5v7" stroke="#fff"/></svg>www.vorumbra-example.com</li>
      </ul>
    </div>
  </section>
</body>
</html>
```